Trading company need to develop packaging design for a new nuts brand.

We need a packaging design for a new nuts brand.
- Packaging format - doypack packaging with zip lock 150 g - 150x220mm
- Product line will include all possible types of nuts. We would like to take a pistachio like an exampl for developing design.
- The main task is to connect the whole concept to the Verdelle character /hero (Example of the image is in Uploaded files, but you don't need to use it)
- In design we expect modern, creative and non-standard solutions, we focus on minimalism
- Packaging mustn’t be transparent or craft
- The future product will be a premium segment
- We expect front and back design of packaging
- Our competitors: Brisvane and Holmwacker (Examples of competitors' packaging, I will attach in Uploaded files)
- Future brand would be sold in different countries therefore the design must be universal, not connect to any region, country or place of nuts growth.
Look and feel
Each slider illustrates characteristics of the customer's brand and the style your logo design should communicate.

```html
<!DOCTYPE html>
<html lang="en">
<head>
<meta charset="utf-8">
<title>Verdelle Pistachio Pouch – Front</title>
<link href="https://fonts.googleapis.com/css2?family=Jost:wght@400;500;600;700&display=swap" rel="stylesheet">
<style>
  :root {
    --stage: #cdbd98;
    --sky: #35a9e6;
    --sky-soft: #bfe0ee;
    --clay: #8f5a4c;
    --violet: #8c84b4;
    --amber: #e39a35;
    --sun: #fbc93c;
    --ink-light: #ffffff;
    --ink-soft: rgba(255,255,255,0.82);
    --brand-blue: #2a9fdd;
    --nut-green: #7f9b3a;
    --nut-shell: #c99a6c;
    --satin-hi: rgba(240,240,246,0.8);
    --satin-lo: rgba(196,195,208,0.45);
  }
  * { margin: 0; padding: 0; box-sizing: border-box; }
  html, body {
    width: 1200px; height: 800px; overflow: hidden;
    background: var(--stage);
    font-family: "Jost", "Futura", sans-serif;
  }
  .canvas { position: relative; width: 1200px; height: 800px; }

  .pouch {
    position: absolute; left: 356px; top: 40px;
    width: 488px; height: 720px;
    border-radius: 22px;
    overflow: hidden;
    background:
      radial-gradient(ellipse 45% 30% at 50% 22%, rgba(255,238,170,0.95), rgba(255,238,170,0) 100%),
      radial-gradient(ellipse 30% 25% at 72% 70%, rgba(255,250,190,0.9), rgba(255,250,190,0) 100%),
      radial-gradient(ellipse 40% 60% at 0% 55%, var(--clay), rgba(143,90,76,0) 100%),
      radial-gradient(ellipse 35% 55% at 100% 40%, var(--violet), rgba(140,132,180,0) 100%),
      radial-gradient(ellipse 60% 30% at 85% 100%, var(--sun), rgba(251,201,60,0) 100%),
      linear-gradient(180deg, var(--sky) 0%, var(--sky-soft) 12%, #f3cfa0 28%, #d99a72 50%, #d8914c 78%, var(--amber) 100%);
  }
  .pouch-notch {
    position: absolute; top: 100px; width: 10px; height: 10px;
    border-radius: 50%; background: var(--stage);
  }
  .pouch-notch--left { left: -5px; }
  .pouch-notch--right { right: -5px; }

  .brand-dot {
    position: absolute; left: 232px; top: 100px;
    width: 24px; height: 24px; border-radius: 50%;
    background: var(--brand-blue);
  }
  .brand-name {
    position: absolute; left: 0; width: 100%; top: 128px;
    text-align: center;
    font-size: 34px; line-height: 40px; font-weight: 600; color: var(--brand-blue);
  }

  .ribbon-art {
    position: absolute; left: 0; top: 190px; width: 488px; height: 170px;
    background: radial-gradient(ellipse 55% 50% at 50% 50%, var(--satin-hi), var(--satin-lo) 55%, rgba(196,195,208,0) 100%);
  }
  .hero-nuts {
    position: absolute; left: 176px; top: 262px; width: 144px; height: 96px;
    border-radius: 50%;
    background: radial-gradient(ellipse at 50% 55%, var(--nut-shell), #9a6a48 60%, rgba(127,155,58,0) 100%);
  }

  .product-name {
    position: absolute; left: 0; width: 100%; top: 370px;
    text-align: center;
    font-size: 33px; line-height: 38px; font-weight: 600; color: var(--ink-light);
    letter-spacing: 1px;
  }
  .net-weight {
    position: absolute; left: 0; width: 100%;
    text-align: center;
    font-size: 11px; line-height: 14px; font-weight: 600; color: var(--ink-light);
  }
  .net-weight--main { top: 416px; left: -4px; }
  .net-weight--foot { top: 691px; }

  .tagline {
    position: absolute; left: 25px; top: 492px;
    font-size: 11px; font-weight: 500; line-height: 14px;
    color: var(--ink-light); letter-spacing: 0.6px;
  }
  .story {
    position: absolute; left: 25px; top: 548px; width: 124px;
    font-size: 6.5px; line-height: 9.5px; color: var(--ink-soft);
  }

  .cert-badge { position: absolute; left: 350px; top: 494px; width: 50px; height: 52px; }

  .feature-strip {
    position: absolute; left: 70px; top: 604px; width: 360px; height: 66px;
    display: flex; justify-content: space-between; align-items: center;
    background: linear-gradient(90deg, rgba(255,255,255,0), rgba(255,255,255,0.12) 20%, rgba(255,255,255,0.12) 80%, rgba(255,255,255,0));
  }
  .feature { display: flex; align-items: center; gap: 6px; width: 116px; }
  .feature-icon { flex: none; width: 30px; height: 30px; }
  .feature-title { font-size: 9.5px; font-weight: 700; color: var(--ink-light); line-height: 10px; }
  .feature-lead { font-size: 5.5px; font-weight: 600; color: var(--ink-light); line-height: 7px; }
  .feature-text { font-size: 4.5px; color: var(--ink-soft); line-height: 5.5px; }
</style>
</head>
<body>
<main class="canvas">
  <section class="pouch">
    <span class="pouch-notch pouch-notch--left"></span>
    <span class="pouch-notch pouch-notch--right"></span>

    <span class="brand-dot"></span>
    <h1 class="brand-name">Verdelle</h1>

    <div class="ribbon-art" role="img" aria-label="Flowing silver satin ribbon sweeping across the pouch"></div>
    <div class="hero-nuts" role="img" aria-label="Photograph of shelled pistachios with green leaves"></div>

    <h2 class="product-name">PISTACHIO</h2>
    <p class="net-weight net-weight--main">Net Wt. 150g</p>

    <p class="tagline">MADE<br>WITH<br>PASSION</p>
    <p class="story">Lorem ipsum dolor sit amet, consectetur adipiscing elit. Aenean auctor arcu aliquet dui pretium ut feugiat est varius. Quisque</p>

    <svg class="cert-badge" viewBox="0 0 50 52" aria-hidden="true">
      <circle cx="25" cy="20" r="17" fill="none" stroke="var(--ink-light)" stroke-width="1.5"/>
    </svg>

    <div class="feature-strip">
      <div class="feature">
        <svg class="feature-icon" viewBox="0 0 30 30" aria-hidden="true"><circle cx="15" cy="15" r="12" fill="none" stroke="#fff" stroke-width="1.2"/></svg>
        <div>
          <p class="feature-title">LOREM IPSUM</p>
          <p class="feature-lead">Lorem ipsum dolor sit amet</p>
          <p class="feature-text">Gently roasted in small batches for a rich and even taste.</p>
        </div>
      </div>
      <div class="feature">
        <svg class="feature-icon" viewBox="0 0 30 30" aria-hidden="true"><circle cx="15" cy="15" r="12" fill="none" stroke="#fff" stroke-width="1.2"/></svg>
        <div>
          <p class="feature-title">LOREM IPSUM</p>
          <p class="feature-lead">Lorem ipsum dolor sit amet</p>
          <p class="feature-text">Only whole nuts, with nothing added and nothing taken away.</p>
        </div>
      </div>
      <div class="feature">
        <svg class="feature-icon" viewBox="0 0 30 30" aria-hidden="true"><circle cx="15" cy="15" r="12" fill="none" stroke="#fff" stroke-width="1.2"/></svg>
        <div>
          <p class="feature-title">LOREM IPSUM</p>
          <p class="feature-lead">Lorem ipsum dolor sit amet</p>
          <p class="feature-text">Sealed fresh in a resealable pouch to keep every crunch.</p>
        </div>
      </div>
    </div>

    <p class="net-weight net-weight--foot">Net Wt. 150g</p>
  </section>
</main>
</body>
</html>
```